New business card design to go with our new logo

just want an eye-catching business card to go with our new logo. We are open to double sided or single sided. Just want it to have the following info on it. Whatever layout you think looks best.

First and Last Name
Title
Phone 801-555-0187
Address 312 W. Larkmoor Avenue Orem UT 84057
Email thecrew@meadowstailandkennel.example

Industry/Entity Type

Business

```html
<!DOCTYPE html>
<html lang="en">
<head>
<meta charset="utf-8">
<title>Meadow's Tail & Kennel — Business Card</title>
<link href="https://fonts.googleapis.com/css2?family=Work+Sans:wght@400;500&display=swap" rel="stylesheet">
<style>
  :root {
    --page: #1c1c1c;
    --card: #252525;
    --ink: #f1f1f1;
    --silver: #b4b4b4;
    --blue: #2aa0d8;
    --orange: #f38a44;
  }
  * { box-sizing: border-box; margin: 0; padding: 0; }
  html, body { width: 1200px; height: 900px; overflow: hidden; background: var(--page); }
  body { font-family: "Work Sans", sans-serif; color: var(--ink); position: relative; }

  .card {
    position: absolute; left: 270px; width: 660px; height: 377px;
    background: var(--card); box-shadow: 0 14px 30px rgba(0,0,0,.55);
  }
  .card--front { top: 46px; }
  .card--back { top: 477px; }

  /* front */
  .front-brand {
    position: absolute; left: 0; right: 0; top: 118px; text-align: center;
    font-size: 46px; font-weight: 500; color: var(--silver); white-space: nowrap;
  }
  .front-brand-dot {
    display: block; width: 14px; height: 14px; margin: 0 auto 22px;
    background: var(--silver); border-radius: 50%;
  }
  .front-url {
    position: absolute; left: 0; right: 0; top: 262px; text-align: center;
    font-size: 18px; letter-spacing: 1.5px; color: var(--ink); white-space: nowrap;
  }
  .front-url .domain { color: var(--blue); }

  /* back */
  .back-brand {
    position: absolute; left: 20px; top: 168px; width: 280px; text-align: center;
    font-size: 22px; font-weight: 500; color: var(--orange); white-space: nowrap;
  }
  .divider { position: absolute; left: 310px; top: 80px; width: 2px; height: 200px; background: var(--orange); }
  .contact { position: absolute; left: 336px; top: 88px; width: 310px; }
  .contact-name { font-size: 22px; color: var(--blue); text-transform: uppercase; letter-spacing: 1px; }
  .contact-title { font-size: 15px; margin-top: 2px; }
  .contact-address { font-size: 14.5px; margin-top: 16px; line-height: 1.35; }
  .contact-list { list-style: none; margin-top: 16px; font-size: 13.5px; }
  .contact-list li { display: flex; align-items: center; gap: 10px; line-height: 1.6; white-space: nowrap; }
  .contact-list svg { width: 13px; height: 13px; fill: var(--blue); flex: none; }
</style>
</head>
<body>
  <section class="card card--front">
    <div class="front-brand"><span class="front-brand-dot"></span>Meadow's Tail &amp; Kennel</div>
    <div class="front-url">www.<span class="domain">meadowstailandkennel</span>.example</div>
  </section>

  <section class="card card--back">
    <div class="back-brand">Meadow's Tail &amp; Kennel</div>
    <div class="divider"></div>
    <div class="contact">
      <div class="contact-name">Daniel Reyes</div>
      <div class="contact-title">Managing Director</div>
      <div class="contact-address">312 W. Larkmoor Avenue<br>Orem UT 84057</div>
      <ul class="contact-list">
        <li><svg viewBox="0 0 24 24"><path d="M6.6 10.8a15.1 15.1 0 0 0 6.6 6.6l2.2-2.2a1 1 0 0 1 1-.25 11.4 11.4 0 0 0 3.6.57 1 1 0 0 1 1 1V20a1 1 0 0 1-1 1A17 17 0 0 1 3 4a1 1 0 0 1 1-1h3.5a1 1 0 0 1 1 1c0 1.25.2 2.45.57 3.6a1 1 0 0 1-.25 1z"/></svg>801-555-0187</li>
        <li><svg viewBox="0 0 24 24"><path d="M2 5h20v14H2zm2 2v.5l8 5 8-5V7z"/></svg>thecrew@meadowstailandkennel.example</li>
        <li><svg viewBox="0 0 24 24"><path d="M12 2a10 10 0 1 0 0 20 10 10 0 0 0 0-20zm0 2c.9 0 2.2 2 2.7 5H9.3C9.8 6 11.1 4 12 4zM4.3 11h3a20 20 0 0 0 0 2h-3a8 8 0 0 1 0-2zm5 0h5.4a17 17 0 0 1 0 2H9.3a17 17 0 0 1 0-2zm7.4 0h3a8 8 0 0 1 0 2h-3a20 20 0 0 0 0-2zM9.3 15h5.4c-.5 3-1.8 5-2.7 5s-2.2-2-2.7-5z"/></svg>www.meadowstailandkennel.example</li>
      </ul>
    </div>
  </section>
</body>
</html>
```